Business card for auto dealership

Looking for a clean modern design.
Would like attached logo incorporated

Industry/Entity Type

Car dealership

Contact Information for Business Card

Name, website, phone, cell, fax, email

```html
<!DOCTYPE html>
<html lang="en">
<head>
<meta charset="utf-8">
<title>Harlan Truck &amp; Auto Sales – Business Card</title>
<link href="https://fonts.googleapis.com/css2?family=Montserrat:wght@400;500;700&display=swap" rel="stylesheet">
<style>
  :root {
    --canvas: #efefef;
    --ink: #000000;
    --paper: #ffffff;
    --text: #111111;
    --sheen-dark: rgba(255,255,255,0.22);
    --sheen-light: #ececec;
    --shadow: rgba(0,0,0,0.28);
  }
  * { margin: 0; padding: 0; box-sizing: border-box; }
  html, body { width: 1200px; height: 1200px; overflow: hidden; }
  body {
    background: var(--canvas);
    font-family: "Montserrat", sans-serif;
    position: relative;
  }
  .card {
    position: absolute;
    overflow: hidden;
    box-shadow: 0 4px 14px var(--shadow);
  }
  .card-front { left: 52px; top: 130px; width: 800px; height: 456px; background: var(--paper); }
  .card-back { left: 315px; top: 613px; width: 801px; height: 455px; background: var(--ink); }

  .brand-panel { position: absolute; left: 0; top: 0; width: 348px; height: 456px; background: var(--ink); }

  .texture { position: absolute; }
  .card-front .texture-dark {
    left: 0; top: 260px; width: 348px; height: 196px;
    background: linear-gradient(to top, var(--sheen-dark), rgba(255,255,255,0));
  }
  .card-front .texture-light {
    left: 348px; top: 260px; width: 452px; height: 196px;
    background: linear-gradient(to top, var(--sheen-light), rgba(236,236,236,0));
  }
  .card-back .texture-dark {
    left: 0; top: 170px; width: 801px; height: 285px;
    background: radial-gradient(ellipse at 85% 100%, rgba(255,255,255,0.16), rgba(255,255,255,0) 65%);
  }

  .brand { position: absolute; color: var(--paper); font-weight: 700; text-align: center; line-height: 1; }
  .brand-name { display: block; letter-spacing: 1px; }
  .brand-tag { display: block; letter-spacing: 0.5px; }
  .card-front .brand { left: 0; width: 348px; top: 172px; }
  .card-front .brand-name { font-size: 54px; }
  .card-front .brand-tag { font-size: 13px; margin-top: 8px; }
  .card-back .brand { left: 0; width: 801px; top: 135px; }
  .card-back .brand-name { font-size: 88px; }
  .card-back .brand-tag { font-size: 20px; margin-top: 12px; }

  .person { position: absolute; left: 399px; top: 62px; color: var(--text); }
  .person-name { font-size: 34px; font-weight: 700; letter-spacing: 0.3px; }
  .person-title { font-size: 28px; font-weight: 400; margin-top: 2px; }

  .contact-list { position: absolute; left: 398px; top: 158px; list-style: none; }
  .contact-item { display: flex; align-items: center; height: 49px; font-size: 22px; font-weight: 500; color: var(--text); }
  .contact-item svg { width: 30px; height: 30px; margin-right: 18px; flex: none; }
  .website { position: absolute; left: 400px; top: 371px; font-size: 21px; font-weight: 500; color: var(--text); }
  .card-back .website { left: 0; width: 801px; text-align: center; top: 372px; color: var(--paper); font-size: 25px; font-weight: 400; }
</style>
</head>
<body>

<section class="card card-front">
  <div class="brand-panel"></div>
  <div class="texture texture-dark" role="img" aria-label="Diagonal silver stripe texture fading up from the bottom"></div>
  <div class="texture texture-light" role="img" aria-label="Faint grey diagonal stripe texture"></div>

  <div class="brand">
    <span class="brand-name">HARLAN</span>
    <span class="brand-tag">TRUCK &amp; AUTO SALES</span>
  </div>

  <div class="person">
    <div class="person-name">Daniel Reyes</div>
    <div class="person-title">General Manager</div>
  </div>

  <ul class="contact-list">
    <li class="contact-item">
      <svg viewBox="0 0 30 30"><circle cx="15" cy="15" r="15" fill="#111"/><rect x="8" y="10" width="14" height="10" rx="1" fill="none" stroke="#fff" stroke-width="1.8"/><path d="M8.5 10.5 15 16l6.5-5.5" fill="none" stroke="#fff" stroke-width="1.8"/></svg>
      yourname@harlan.com
    </li>
    <li class="contact-item">
      <svg viewBox="0 0 30 30"><circle cx="15" cy="15" r="15" fill="#111"/><path d="M10 8.5c1-.8 2-.6 2.5.3l1.4 2.4c.4.7.2 1.4-.4 1.9l-.9.7c.7 1.6 2 3 3.6 3.8l.8-.9c.5-.6 1.3-.7 1.9-.3l2.4 1.5c.8.5.9 1.6.2 2.4-1 1.1-2.4 1.6-3.800 1.1C13.3 20.2 9.8 16.6 8.5 12.3c-.3-1.4.4-2.9 1.5-3.8z" fill="#fff"/></svg>
      +1 (555) 010-2040
    </li>
    <li class="contact-item">
      <svg viewBox="0 0 30 30"><circle cx="15" cy="15" r="15" fill="#111"/><rect x="10.5" y="7" width="9" height="16" rx="1.5" fill="none" stroke="#fff" stroke-width="1.8"/><circle cx="15" cy="20" r="1" fill="#fff"/></svg>
      0857 0000 1122
    </li>
    <li class="contact-item">
      <svg viewBox="0 0 30 30"><circle cx="15" cy="15" r="15" fill="#111"/><rect x="10.5" y="7.5" width="9" height="5" fill="#fff"/><rect x="7.5" y="12" width="15" height="7" rx="1.5" fill="#fff"/><rect x="10.5" y="17" width="9" height="6" fill="#fff" stroke="#111" stroke-width="1.2"/></svg>
      +1 (555) 010-3090
    </li>
  </ul>

  <div class="website">www.harlanauto.com</div>
</section>

<section class="card card-back">
  <div class="texture texture-dark" role="img" aria-label="Soft silver diagonal stripe texture in the lower right"></div>

  <div class="brand">
    <span class="brand-name">HARLAN</span>
    <span class="brand-tag">TRUCK &amp; AUTO SALES</span>
  </div>

  <div class="website">www.harlanauto.com</div>
</section>

</body>
</html>
```